Fernvale Craft Works business card design- Fine Art sculpture business (Contract guaranteed)

This business card is for a fine art business. Though we don't have a website up and running yet it should be up soon. I would like the business card to be elegant and fairly simple with a picture of one of my sculptures on the front (you might need to photoshop out the background) as well as my basic contact info (my name,phone # and e-mail). On the back I'd like it to be pretty simple with just "Notes" and some blank lines for writing in info.

Target Market(s)

High end artwork buyers

Industry/Entity Type

Art Gallery

Contact Information for Business Card

Marlo Prewitt Phone: (555) 213-4098 E-mail: marlo@quillbrookmail.com Facebook: @fernvalecraftworks Instagram: fernvalecraftworks

Colors

Designer to choose colors to be used in the design.

Requirements
Must have
• *A picture of one of my sculptures*, my name, business name (Fernvale Craft Works), e-mail, phone #, and a notes section on the back.
• Fernvale Craft Works
• Marlo Prewitt
• (555)213-4098
• marlo@quillbrookmail.com
• Facebook: @fernvalecraftworks
• Instagram: fernvalecraftworks
Nice to have
• It'd be nice if you can crop out the background in the sculpture pictures, which ever one you end up using.

```html
<!DOCTYPE html>
<html lang="en">
<head>
<meta charset="utf-8">
<title>Fernvale Craft Works – Business Card</title>
<link rel="stylesheet" href="https://fonts.googleapis.com/css2?family=Bebas+Neue&family=Alegreya:wght@400;500&display=swap">
<style>
  :root {
    --paper: #ffffff;
    --ink: #111111;
    --band: #2b1740;
    --stone-deep: #0d3b2c;
    --stone-mid: #1f7a5a;
    --stone-light: #4fb08c;
    --plinth: #161616;
  }
  * { margin: 0; padding: 0; box-sizing: border-box; }
  html, body {
    width: 1200px;
    height: 667px;
    overflow: hidden;
    background: var(--paper);
  }
  .card {
    position: relative;
    width: 1200px;
    height: 667px;
    background: var(--paper);
    color: var(--ink);
  }
  .sculpture-photo {
    position: absolute;
    left: 172px;
    top: 34px;
    width: 228px;
    height: 594px;
    border-radius: 48% 42% 30% 30% / 30% 30% 8% 8%;
    background:
      radial-gradient(ellipse at 45% 35%, var(--stone-light) 0%, var(--stone-mid) 40%, var(--stone-deep) 80%),
      var(--stone-deep);
  }
  .sculpture-photo::after {
    content: "";
    position: absolute;
    left: 8px;
    right: 8px;
    bottom: 0;
    height: 74px;
    border-radius: 50% / 30%;
    background: var(--plinth);
  }
  .identity {
    position: absolute;
    left: 560px;
    top: 140px;
    width: 520px;
    text-align: center;
  }
  .studio-name {
    font-family: "Bebas Neue", "Oswald", sans-serif;
    font-weight: 400;
    line-height: 1;
  }
  .studio-name__main {
    display: block;
    font-size: 104px;
    letter-spacing: 1px;
  }
  .studio-name__sub {
    display: block;
    margin-top: 10px;
    font-size: 48px;
    letter-spacing: 0.32em;
    padding-left: 0.32em;
  }
  .divider {
    width: 354px;
    height: 3px;
    margin: 18px auto 0;
    background: var(--ink);
  }
  .contact {
    font-family: "Alegreya", "Georgia", serif;
    font-style: normal;
  }
  .contact__name {
    margin-top: 22px;
    font-size: 46px;
    font-weight: 400;
    letter-spacing: 0.5px;
  }
  .contact__phone {
    margin-top: 18px;
    font-size: 31px;
    font-weight: 500;
  }
  .contact__email {
    margin-top: 14px;
    font-size: 31px;
    font-weight: 500;
  }
  .base-band {
    position: absolute;
    left: 0;
    bottom: 0;
    width: 100%;
    height: 18px;
    background: var(--band);
  }
</style>
</head>
<body>
  <main class="card">
    <div class="sculpture-photo" role="img" aria-label="Photograph of a polished green malachite stone sculpture on a round black base"></div>

    <section class="identity">
      <h1 class="studio-name">
        <span class="studio-name__main">Fernvale</span>
        <span class="studio-name__sub">Craft Works</span>
      </h1>
      <div class="divider"></div>
      <address class="contact">
        <p class="contact__name">Marlo Prewitt</p>
        <p class="contact__phone">(555)213-4098</p>
        <p class="contact__email">marlo.prewitt4@quillbrookmail.com</p>
      </address>
    </section>

    <div class="base-band"></div>
  </main>
</body>
</html>
```